Stonebay Towing Business Card

Towing
Accident towing
Mechanical breakdown
Insurance, salvage and recovery
4wd off road towing
Light & Heavy towing
8347 2516
24 hour business 7 days

Logo can be whole size on front

Industry/Entity Type

Towing/ transport

Contact Information for Business Card

The above

```html
<!DOCTYPE html>
<html lang="en">
<head>
<meta charset="utf-8">
<title>Stonebay Towing Business Card</title>
<link rel="stylesheet" href="https://fonts.googleapis.com/css2?family=Montserrat:wght@400;700&display=swap">
<style>
  :root {
    --backdrop: #3a3a3c;
    --card: #f1f1f1;
    --ink: #2a2a2a;
    --brand-red: #c8141c;
  }
  * { margin: 0; padding: 0; box-sizing: border-box; }
  html, body { width: 1200px; height: 1059px; overflow: hidden; }
  body {
    position: relative;
    background: var(--backdrop);
    font-family: "Montserrat", sans-serif;
    color: var(--ink);
  }
  .card {
    position: absolute;
    background: var(--card);
    border-radius: 22px;
    box-shadow: 0 10px 18px rgba(0,0,0,0.45);
  }
  .card--back { left: 256px; top: 100px; width: 688px; height: 393px; }
  .card--front { left: 253px; top: 536px; width: 694px; height: 396px; }

  .brand-name {
    position: absolute;
    font-weight: 700;
    color: var(--brand-red);
    line-height: 1;
    white-space: nowrap;
  }
  .card--back .brand-name { left: 38px; top: 56px; font-size: 38px; }
  .card--front .brand-name {
    left: 0; right: 0; top: 170px;
    text-align: center;
    font-size: 64px;
  }

  .service-list {
    position: absolute;
    left: 36px; top: 176px;
    list-style: none;
    font-size: 19px;
    font-weight: 400;
  }
  .service-list li {
    position: relative;
    padding-left: 19px;
    height: 32.7px;
    line-height: 26px;
  }
  .service-list li::before {
    content: "";
    position: absolute;
    left: 0; top: 8px;
    width: 11px; height: 11px;
    border-radius: 50%;
    background: var(--brand-red);
  }

  .contact {
    position: absolute;
    left: 380px; top: 176px;
    width: 296px;
    text-align: center;
    font-size: 20px;
    font-weight: 400;
  }
  .contact__hours { line-height: 26px; }
  .contact__phone {
    margin-top: 8px;
    display: inline-flex;
    align-items: center;
    gap: 8px;
    line-height: 26px;
  }
  .contact__phone svg { width: 24px; height: 24px; }
</style>
</head>
<body>
  <section class="card card--back">
    <div class="brand-name">Stonebay Towing</div>
    <ul class="service-list">
      <li>Towing</li>
      <li>Accident towing</li>
      <li>Mechanical breakdown</li>
      <li>Insurance, salvage and recovery</li>
      <li>4wd off road towing</li>
      <li>Light &amp; Heavy towing</li>
    </ul>
    <div class="contact">
      <p class="contact__hours">24 hour business 7 days</p>
      <p class="contact__phone">
        <svg viewBox="0 0 24 24" aria-hidden="true">
          <path fill="var(--brand-red)" d="M6.6 3.2c.5-.5 1.3-.5 1.8 0l2.2 2.6c.4.5.4 1.2 0 1.7l-1.3 1.4c.9 2 2.5 3.7 4.6 4.7l1.4-1.3c.5-.4 1.2-.4 1.7 0l2.6 2.2c.5.5.5 1.3 0 1.8l-1.6 1.7c-.9.9-2.3 1.2-3.5.7C9 16.6 5.4 13 3.5 8.4c-.5-1.2-.2-2.6.7-3.5z"/>
          <path fill="none" stroke="var(--brand-red)" stroke-width="1.8" stroke-linecap="round" d="M14 3.5a7 7 0 0 1 6.5 6.5M14 7a3.5 3.5 0 0 1 3 3"/>
        </svg>
        <span>8347 2516</span>
      </p>
    </div>
  </section>

  <section class="card card--front">
    <div class="brand-name">Stonebay Towing</div>
  </section>
</body>
</html>
```